Website Design for Employee Moral and Happiness Company

Looking for a clean website design that explains our features in a step by step manner so our visitors know exactly what our site does before logging in.

The site is called "Velquo". See logo design and video for a sample of style and an overview of what we do.

Target Market(s)

Business owners that are looking to retain employees.

Number of Pages Required

1 page

```html
<!DOCTYPE html>
<html lang="en">
<head>
<meta charset="utf-8">
<title>Velquo – Start Building Your Event</title>
<link rel="stylesheet" href="https://fonts.googleapis.com/css2?family=Gelasio:wght@400;600;700&family=Poppins:ital,wght@0,400;0,500;0,600;1,500;1,600&display=swap">
<style>
:root{
  --orange:#f5811f;
  --peach:#fde3d1;
  --ink:#141414;
  --grey:#555;
  --navy:#0c0f1f;
  --white:#fff;
}
*{margin:0;padding:0;box-sizing:border-box}
html,body{width:1200px;height:4084px;overflow:hidden;background:var(--white)}
body{position:relative;font-family:"Poppins",sans-serif;color:var(--ink)}
.abs{position:absolute}
.band{position:absolute;left:0;width:1200px}
.band-hero{top:0;height:715px;background:linear-gradient(180deg,var(--orange) 0%,var(--orange) 70%,#f79445 100%)}
.band-features{top:1560px;height:833px;background:var(--peach)}
.band-demo{top:2393px;height:490px;background:linear-gradient(180deg,var(--orange) 0%,var(--orange) 75%,#f79445 100%)}
.band-footer{top:3800px;height:240px;background:var(--navy)}

/* header */
.logo{font-family:"Gelasio",serif;font-weight:700;color:var(--white);letter-spacing:1px}
.site-logo{left:60px;top:8px;font-size:48px}
.nav{left:436px;top:32px;display:flex;gap:28px;font-size:11px;color:var(--white)}
.nav a{color:inherit;text-decoration:none}
.nav .active{color:var(--ink)}
.login{left:945px;top:31px;font-size:12px;color:var(--white)}
.btn{display:flex;align-items:center;justify-content:center;border-radius:30px;font-family:"Gelasio",serif;font-weight:600;text-decoration:none}
.btn-white{background:var(--white);color:var(--orange)}
.btn-orange{background:var(--orange);color:var(--white)}
.btn-outline{border:1.5px solid var(--white);color:var(--white)}
.header-demo{left:989px;top:21px;width:150px;height:36px;font-size:15px}

/* hero */
.hero-title{left:0;width:1200px;top:128px;text-align:center;font-style:italic;font-weight:500;font-size:42px;line-height:54px;color:var(--ink)}
.hero-title .light{color:var(--white)}
.hero-art{left:350px;top:268px;width:505px;height:420px;border-radius:24px;background:linear-gradient(160deg,#f4ece6,#e8dcd2 60%,#c9b9ad)}

/* section headings */
.sec-title{left:0;width:1200px;text-align:center;font-family:"Gelasio",serif;font-weight:600;font-size:31px}
.sec-text{left:330px;width:540px;text-align:center;font-size:11.5px;line-height:20px;color:var(--grey)}

/* what we do */
.wwd-list{right:772px;top:996px;text-align:right;font-size:13px;color:var(--grey)}
.wwd-list li{list-style:none;height:35px;line-height:20px}
.wwd-list .strong{font-family:"Gelasio",serif;font-weight:600;font-size:19px;color:var(--ink);height:46px;line-height:26px}
.phone{left:499px;top:910px;width:204px;height:444px;border:4px solid #1f2433;border-radius:22px;background:var(--orange);overflow:hidden}
.phone .notch{position:absolute;left:50px;top:2px;width:96px;height:8px;background:#1f2433;border-radius:0 0 8px 8px}
.phone .logo{position:absolute;left:0;width:100%;text-align:center;top:56px;font-size:33px}
.phone-video{position:absolute;left:0;top:148px;width:196px;height:155px;background:linear-gradient(140deg,#1d4e72,#2aa6b5 55%,#e9dfd3)}
.phone-band{position:absolute;left:0;top:303px;width:196px;height:32px;background:#b8ada1}
.play{position:absolute;left:78px;top:200px;width:52px;height:52px;border-radius:50%;background:var(--white);display:flex;align-items:center;justify-content:center}
.play span{width:44px;height:44px;border-radius:50%;background:#e4212b;display:flex;align-items:center;justify-content:center}
.wwd-right{left:756px;top:1062px;width:340px}
.wwd-right h3{font-family:"Gelasio",serif;font-weight:600;font-size:26px;line-height:32px}
.wwd-right .tag{color:var(--orange);font-size:12px;margin-top:6px}
.wwd-right p{font-size:11.5px;line-height:20px;color:var(--grey);margin-top:18px}
.wwd-demo{left:517px;top:1384px;width:166px;height:41px;font-size:15px}

/* features */
.feature{width:260px;text-align:center}
.feature .ring{width:166px;height:166px;margin:0 auto;border-radius:50%;border:6px solid var(--orange);overflow:hidden}
.feature .art{width:100%;height:100%}
.feature h4{font-family:"Gelasio",serif;font-weight:700;font-size:15px;margin-top:14px}

/* demo */
.demo-title{color:var(--white);font-size:37px}
.demo-text{color:var(--white);left:360px;width:480px}
.email-field{left:368px;top:2580px;width:464px;height:41px;border-radius:12px;background:var(--white);font-size:11px;color:#666;padding:13px 17px}
.demo-btn{left:510px;top:2638px;width:180px;height:40px;font-size:16px}

/* know more */
.km-title{left:62px;top:2940px;font-family:"Gelasio",serif;font-weight:600;font-size:31px;line-height:37px}
.km-arrows{left:1030px;top:2950px}
.card{top:3062px;height:292px}
.card.dark{background:linear-gradient(160deg,#2b2e3b,#3e4050 60%,#2a2c35)}
.card .cap{position:absolute;left:0;right:0;bottom:22px;text-align:center;font-size:13.5px;color:var(--orange)}
.card.light{background:#ebe1d7}
.card .art{position:absolute;left:14px;top:44px;width:190px;height:195px;border-radius:6px;background:linear-gradient(150deg,#f2e9e0,#9ccabf 55%,#f38b2c)}
.card .body{position:absolute;left:219px;top:46px;width:180px}
.card .body h5{font-family:"Gelasio",serif;font-weight:600;font-size:23px;line-height:30px}
.card .body p{font-size:11px;line-height:20px;color:var(--grey);margin-top:20px}

/* cta */
.cta-title{top:3540px;font-size:30px;line-height:42px}
.cta-btn{left:502px;top:3633px;width:195px;height:38px;font-size:15px}

/* footer */
.foot-logo{left:60px;top:3840px;font-size:60px}
.foot-tag{left:67px;top:3920px;font-size:11px;color:var(--orange)}
.foot-btn{left:92px;top:3951px;width:195px;height:40px;font-size:15px}
.foot-col{top:3840px;color:var(--white)}
.foot-col h6{font-family:"Gelasio",serif;font-weight:600;font-size:17px;margin-bottom:16px}
.foot-col li{list-style:none;font-size:10.5px;height:22.5px;display:flex;align-items:center;gap:11px}
.foot-col li::before{content:"";width:6px;height:6px;border-radius:50%;border:1.5px solid var(--orange)}
.contact-row{display:flex;align-items:center;gap:16px;font-size:11.5px;height:32px}
.socials{display:flex;gap:8px;margin-top:12px}
.socials span{width:35px;height:35px;border-radius:50%;background:var(--orange);display:block}
.copyright{left:0;top:4037px;width:1200px;height:47px;background:var(--orange);color:var(--white);font-size:11px;text-align:center;line-height:47px}
</style>
</head>
<body>

<div class="band band-hero" aria-hidden="true"></div>
<div class="band band-features" aria-hidden="true"></div>
<div class="band band-demo" aria-hidden="true"></div>
<div class="band band-footer" aria-hidden="true"></div>

<header>
  <div class="abs logo site-logo">Velquo</div>
  <nav class="abs nav">
    <a class="active" href="#">Home</a><a href="#">What We Do</a><a href="#">Feature</a><a href="#">Contact</a><a href="#">Resources</a>
  </nav>
  <div class="abs login">Login</div>
  <a class="abs btn btn-white header-demo" href="#">Request A Demo</a>
</header>

<section class="hero">
  <h1 class="abs hero-title">Start <span class="light">Building Your Event</span><br>Today With Me !</h1>
  <div class="abs hero-art" role="img" aria-label="Illustration of a team meeting around a table with a phone showing the app"></div>
</section>

<section class="what-we-do">
  <h2 class="abs sec-title" style="top:780px">What We Do</h2>
  <p class="abs sec-text" style="top:834px">Lorem Ipsum has been the industry's standard dummy text ever since the, when an unknown printer took a galley type and scrambled type specimen book.</p>
  <ul class="abs wwd-list">
    <li>Worried About Events</li>
    <li>Worried Employee Moral</li>
    <li class="strong">Let's Start With Velquo</li>
    <li>My Event Planner</li>
    <li>Increase Employee Relation</li>
    <li>From Raffles To Auctions</li>
    <li>Transform Your Work Events</li>
    <li>Boost Employee Morale</li>
  </ul>
  <div class="abs phone">
    <div class="notch"></div>
    <div class="logo">Velquo</div>
    <div class="phone-video" role="img" aria-label="Video still of a person working at a laptop"></div>
    <div class="phone-band"></div>
    <div class="play"><span><svg width="16" height="18" viewBox="0 0 16 18"><path d="M2 1 L15 9 L2 17 Z" fill="#fff"/></svg></span></div>
  </div>
  <div class="abs wwd-right">
    <h3>Let's Start With Velquo</h3>
    <div class="tag">I am here To Help Businesses Like Yours.</div>
    <p>Lorem Ipsum has been the industry's standard dummy text ever since the, when an unknown printer took a galley type and scrambled type specimen book.</p>
  </div>
  <a class="abs btn btn-orange wwd-demo" href="#">Request A Demo</a>
</section>

<section class="features">
  <h2 class="abs sec-title" style="top:1733px">Our Features</h2>
  <p class="abs sec-text" style="top:1786px">Lorem Ipsum has been the industry's standard dummy text ever since the, when an unknown printer took a galley type and scrambled type specimen book.</p>
  <div class="abs feature" style="left:168px;top:1868px"><div class="ring"><div class="art" role="img" aria-label="Illustration of coworkers shaking hands" style="background:linear-gradient(140deg,#fdf3ea,#e6b7c4 50%,#2d5a45)"></div></div><h4>Increase Employee Relation</h4></div>
  <div class="abs feature" style="left:469px;top:1868px"><div class="ring"><div class="art" role="img" aria-label="Illustration of an event planner holding papers" style="background:linear-gradient(140deg,#fdf3ea,#e0533d 55%,#25306b)"></div></div><h4>Event Planner</h4></div>
  <div class="abs feature" style="left:767px;top:1868px"><div class="ring"><div class="art" role="img" aria-label="Illustration of people celebrating with a trophy" style="background:linear-gradient(140deg,#eef6f2,#e6a53a 55%,#2d3e5d)"></div></div><h4>Raffles To Auctions</h4></div>
  <div class="abs feature" style="left:168px;top:2114px"><div class="ring"><div class="art" role="img" aria-label="Illustration of a happy group of employees" style="background:linear-gradient(140deg,#fdf3ea,#6aa4d9 50%,#7b4d9b)"></div></div><h4>Boost Employee Morale</h4></div>
  <div class="abs feature" style="left:469px;top:2114px"><div class="ring"><div class="art" role="img" aria-label="Illustration of a person standing among plants" style="background:linear-gradient(140deg,#fdf3ea,#e8b84a 50%,#6fb3d6)"></div></div><h4>Individual Transformation</h4></div>
  <div class="abs feature" style="left:767px;top:2114px"><div class="ring"><div class="art" role="img" aria-label="Illustration of business partners shaking hands" style="background:linear-gradient(140deg,#fdf3ea,#e09b4c 50%,#2e3a5c)"></div></div><h4>Organizational Growth</h4></div>
</section>

<section class="demo">
  <h2 class="abs sec-title demo-title" style="top:2460px">Try Velquo Demo</h2>
  <p class="abs sec-text demo-text" style="top:2520px">Schedule some time with us so we can learn a little bit more about your business needs, and we will tailor a demo to meet your goals.</p>
  <div class="abs email-field">Enter Email *</div>
  <a class="abs btn btn-outline demo-btn" href="#">Schedule A Demo</a>
</section>

<section class="know-more">
  <h2 class="abs km-title">Know More<br>About Velquo</h2>
  <svg class="abs km-arrows" width="110" height="44" viewBox="0 0 110 44" aria-hidden="true">
    <circle cx="24" cy="22" r="20" fill="none" stroke="var(--orange)" stroke-width="1.5"/>
    <path d="M30 16 L16 22 L30 28 Z" fill="var(--orange)"/>
    <line x1="12" y1="22" x2="50" y2="22" stroke="var(--orange)" stroke-width="1.5"/>
    <line x1="68" y1="22" x2="106" y2="22" stroke="var(--ink)" stroke-width="1.5"/>
    <path d="M94 16 L108 22 L94 28 Z" fill="var(--ink)"/>
  </svg>
  <div class="abs card dark" style="left:0;width:239px" role="img" aria-label="Photo of a worried employee in an office chair"><div class="cap">Worried Employee Moral</div></div>
  <div class="abs card light" style="left:263px;width:411px">
    <div class="art" role="img" aria-label="Illustration of a smiling man holding a profile card"></div>
    <div class="body"><h5>Increase Employee Relation</h5><p>Lorem Ipsum been industry's standard dummy ever since the, when an unknown printer galley type &amp; scrambled.</p></div>
  </div>
  <div class="abs card dark" style="left:697px;width:238px" role="img" aria-label="Photo of happy coworkers smiling together"><div class="cap">Happy Employee With Velquo</div></div>
  <div class="abs card dark" style="left:960px;width:240px" role="img" aria-label="Photo of a man working at a desk"><div class="cap">How Velquo Works</div></div>
</section>

<section class="cta">
  <h2 class="abs sec-title cta-title">Ready To Build High-Performing<br>Event With Velquo?</h2>
  <a class="abs btn btn-orange cta-btn" href="#">Get Started With Us</a>
</section>

<footer>
  <div class="abs logo foot-logo">Velquo</div>
  <div class="abs foot-tag">Start Building Your Event Today With Me !</div>
  <a class="abs btn btn-orange foot-btn" href="#">Get Started With Us</a>
  <div class="abs foot-col" style="left:336px">
    <h6>Company</h6>
    <ul><li>What We Do</li><li>Features</li><li>Careers</li><li>Blog</li><li>Contact</li></ul>
  </div>
  <div class="abs foot-col" style="left:612px">
    <h6>Solution</h6>
    <ul><li>Growth &amp; Transformation</li><li>Employee Moral</li><li>Employee Relations</li><li>Diversity, Inclusion &amp; Belonging</li><li>Sales Performance</li></ul>
  </div>
  <div class="abs foot-col" style="left:886px">
    <h6>Contact Us</h6>
    <div class="contact-row"><svg width="18" height="14" viewBox="0 0 18 14"><rect width="18" height="14" rx="2" fill="var(--orange)"/><path d="M1 2 L9 8 L17 2" fill="none" stroke="var(--navy)" stroke-width="1.5"/></svg>info@velquo.com</div>
    <div class="contact-row"><svg width="18" height="18" viewBox="0 0 24 24"><path d="M6.6 10.8a15.1 15.1 0 0 0 6.6 6.6l2.2-2.2a1 1 0 0 1 1-.25 11.4 11.4 0 0 0 3.6.57 1 1 0 0 1 1 1V20a1 1 0 0 1-1 1A17 17 0 0 1 3 4a1 1 0 0 1 1-1h3.5a1 1 0 0 1 1 1c0 1.250.2 2.450.57 3.570a1 1 0 0 1-.25 1z" fill="var(--orange)"/></svg>123 456 7890</div>
    <div class="socials" aria-label="Social links"><span></span><span></span><span></span></div>
  </div>
  <div class="abs copyright">©Velquo - 2022 All rights reserved.</div>
</footer>

</body>
</html>
```